Startup Drone Platform Company business card

We are needing a business card design for our employees. We are a startup drone platform. We are looking for a business card that has our logo on one side, with the employee/company details on the opposite side. We are looking for something that is very eye catching, modern, and bold.

Target Market(s)

This will target both drone pilots and drone businesses, along with all the industries that could utilize drone services (aerial video, aerial photos, inspections, 3d mapping, etc).

Industry/Entity Type

Business

```html
<!DOCTYPE html>
<html lang="en">
<head>
<meta charset="utf-8">
<title>Quadrello business card</title>
<link href="https://fonts.googleapis.com/css2?family=Montserrat:wght@400;500;600;700&display=swap" rel="stylesheet">
<style>
  :root {
    --teal: #33bec9;
    --ink: #1a1a1a;
    --paper: #ffffff;
    --stage: #2c2d2f;
  }
  * { box-sizing: border-box; margin: 0; padding: 0; }
  html, body { width: 1200px; height: 900px; overflow: hidden; background: var(--stage); }
  body { font-family: "Montserrat", sans-serif; position: relative; }

  .card {
    position: absolute;
    left: 300px;
    width: 600px;
    height: 343px;
    border-radius: 24px;
    overflow: hidden;
  }

  /* Front side */
  .card-front { top: 78px; background: var(--teal); }
  .front-brand {
    position: absolute; left: 0; right: 0; top: 120px;
    display: flex; align-items: center; justify-content: center; gap: 14px;
    color: var(--paper); font-weight: 600; font-size: 34px; letter-spacing: 4px;
  }
  .brand-dot {
    width: 22px; height: 22px; border: 3px solid var(--paper); border-radius: 50%; flex: none;
  }
  .front-url {
    position: absolute; left: 0; right: 0; top: 262px; text-align: center;
    color: var(--paper); font-size: 17px; font-weight: 400;
  }
  .front-url strong { color: var(--ink); font-weight: 700; }
  .front-strip-light {
    position: absolute; left: 0; bottom: 0; width: 390px; height: 16px; background: var(--paper);
  }
  .front-strip-dark {
    position: absolute; right: 0; bottom: 0; width: 210px; height: 22px; background: var(--ink);
  }

  /* Back side */
  .card-back { top: 479px; background: var(--paper); }
  .back-wordmark {
    position: absolute; left: 40px; top: 86px;
    display: flex; align-items: center; gap: 8px;
    font-size: 30px; font-weight: 500; letter-spacing: 20px; color: var(--ink);
  }
  .back-wordmark .brand-dot { border-color: var(--teal); width: 24px; height: 24px; }
  .holder {
    position: absolute; right: 38px; top: 150px; width: 240px; text-align: right;
  }
  .holder-name { color: var(--teal); font-size: 22px; font-weight: 600; }
  .holder-role { color: var(--ink); font-size: 12px; margin-top: 1px; }
  .holder-rule { border-top: 1.5px solid var(--ink); margin: 6px 0 10px; }
  .holder-address { color: var(--ink); font-size: 13px; line-height: 1.4; }

  .contact {
    position: absolute; left: 40px; bottom: 40px; width: 300px;
    border-top: 1.5px solid var(--ink); padding-top: 6px;
  }
  .contact-row {
    display: flex; align-items: center; gap: 10px;
    font-size: 14px; color: var(--ink); line-height: 1.45;
  }
  .contact-row svg { width: 11px; height: 11px; flex: none; }
  .contact-row strong { color: var(--teal); font-weight: 600; }

  .back-strip-teal {
    position: absolute; left: 0; bottom: 0; width: 420px; height: 22px; background: var(--teal);
  }
  .back-strip-dark {
    position: absolute; right: 0; bottom: 0; width: 180px; height: 14px; background: var(--ink);
  }
</style>
</head>
<body>

<section class="card card-front">
  <div class="front-brand"><span class="brand-dot"></span>QUADRELLO</div>
  <p class="front-url">www.<strong>QUADRELLO</strong>.com</p>
  <div class="front-strip-light"></div>
  <div class="front-strip-dark"></div>
</section>

<section class="card card-back">
  <div class="back-wordmark"><span>QUADRELLO</span><span class="brand-dot"></span></div>

  <div class="holder">
    <p class="holder-name">Marta Keller</p>
    <p class="holder-role">Director</p>
    <div class="holder-rule"></div>
    <p class="holder-address">48 Harbor Lane<br>Fairview, NY 10980</p>
  </div>

  <div class="contact">
    <p class="contact-row">
      <svg viewBox="0 0 12 12"><path d="M2.5 1 L4.5 1 L5.2 3.4 L4 4.4 Q5 6.8 7.6 8 L8.6 6.8 L11 7.5 L11 9.5 Q10.5 11 9 11 Q1 10 1 2.5 Q1 1 2.5 1Z" fill="var(--teal)"/></svg>
      <span>+330 5170-2294</span>
    </p>
    <p class="contact-row">
      <svg viewBox="0 0 12 12"><rect x="1" y="2.5" width="10" height="7" fill="none" stroke="var(--teal)" stroke-width="1.2"/><path d="M1 2.5 L6 6.5 L11 2.5" fill="none" stroke="var(--teal)" stroke-width="1.2"/></svg>
      <span>info@quadrello.com</span>
    </p>
    <p class="contact-row">
      <svg viewBox="0 0 12 12"><circle cx="6" cy="6" r="5" fill="none" stroke="var(--teal)" stroke-width="1.2"/><ellipse cx="6" cy="6" rx="2.2" ry="5" fill="none" stroke="var(--teal)" stroke-width="1"/><path d="M1 6 H11" stroke="var(--teal)" stroke-width="1"/></svg>
      <span>www.<strong>QUADRELLO</strong>.com</span>
    </p>
  </div>

  <div class="back-strip-teal"></div>
  <div class="back-strip-dark"></div>
</section>

</body>
</html>
```